Email Design Creative Design Needed

Our website is called CampusLedger.org. One of our competitor(varsity scout.us.com) is using the following email creative.
http://pqr.brightquill.com/Affiliate/Assets/3532.html
http://pqr.brightquill.com/Affiliate/Assets/7921.html
http://pqr.brightquill.com/Affiliate/Assets/8061.html

We would like to use similar email creative without copying their exact creative. You can use the above as a guide but then come up with your own version of the creative.
The above are just concepts, please be creative and come up with your own version of it, without feeling that they have been copied. Feel free to move the components around. Also, feel free to change the colours and text.

Please find attached the CampusLedger.org logo.

Reason: We would like to receive more designs.

College

```html
<!DOCTYPE html>
<html lang="en">
<head>
<meta charset="UTF-8">
<title>CampusLedger.org – Education &amp; Teaching Search</title>
<link href="https://fonts.googleapis.com/css2?family=Open+Sans:wght@400;600;700&family=Varela+Round&display=swap" rel="stylesheet">
<style>
  :root {
    --stage: #3a2418;
    --paper: #ffffff;
    --band: #7d7d7d;
    --text-grey: #7a7a7a;
    --logo-grey: #8a8a8a;
    --green-light: #bcd934;
    --green: #95bd17;
    --green-dark: #5f8c0d;
    --pill-top: #ffffff;
    --pill-bottom: #d8d8d8;
    --slate: #5a5a5a;
    --note-bg: rgba(80, 80, 80, 0.72);
  }
  * { box-sizing: border-box; margin: 0; padding: 0; }
  html, body { width: 1200px; height: 1000px; overflow: hidden; }
  body { background: var(--stage); font-family: "Open Sans", Arial, sans-serif; position: relative; }

  .email {
    position: absolute; left: 192px; top: 42px;
    width: 810px; height: 912px;
    background: var(--paper); overflow: hidden;
    box-shadow: 0 10px 30px rgba(0,0,0,0.45);
  }

  .brand {
    position: absolute; top: 16px; left: 0; width: 100%;
    text-align: center;
  }
  .brand-name {
    font-family: "Varela Round", "Open Sans", sans-serif;
    font-size: 44px; color: var(--logo-grey); letter-spacing: -0.5px;
  }

  .title-band {
    position: absolute; top: 79px; left: 0; width: 100%; height: 41px;
    background: var(--band);
    display: flex; align-items: center; justify-content: center;
  }
  .title-band h1 {
    font-family: "Varela Round", "Open Sans", sans-serif;
    font-size: 31px; font-weight: 400; color: #fff;
    -webkit-text-stroke: 0.8px #fff;
  }
  .aid-note {
    position: absolute; top: 125px; left: 0; width: 100%;
    text-align: center; font-size: 12px; color: var(--text-grey);
  }

  .photo {
    position: absolute; left: 0; top: 440px; width: 100%; height: 472px;
    background: linear-gradient(to bottom,
      rgba(255,255,255,1) 0%, #e9ecea 18%, #b9c0b8 34%, #8f9a86 48%,
      #6f8a4c 62%, #5f8f2a 78%, #4f8420 100%);
  }

  .head-band {
    position: absolute; left: 55px; top: 158px; width: 699px; height: 27px;
    background: linear-gradient(to right, var(--green-light), var(--green) 50%, var(--green-light));
  }

  .jobs {
    position: absolute; left: 55px; top: 158px; width: 699px;
    border-collapse: collapse;
  }
  .jobs thead th {
    height: 27px; color: #fff; font-weight: 700; font-size: 16px;
    background: none; text-align: left; padding: 0;
  }
  .jobs th.col-type { padding-left: 28px; width: 287px; }
  .jobs th.col-salary { width: 245px; }
  .jobs th.col-next { padding-left: 27px; }
  .jobs tbody td {
    height: 61px; vertical-align: top; padding-top: 14px;
    font-size: 16px; font-weight: 600; color: var(--text-grey); line-height: 20px;
  }
  .jobs tbody tr:first-child td { padding-top: 14px; }
  .jobs td.job { padding-left: 2px; padding-right: 10px; white-space: nowrap; }
  .jobs td.salary { padding-left: 1px; }
  .jobs td.next { padding-left: 0; padding-top: 13px; }

  .btn {
    display: inline-flex; align-items: center;
    width: 147px; height: 28px; border-radius: 14px;
    background: linear-gradient(to bottom, var(--pill-top), var(--pill-bottom));
    box-shadow: 0 2px 3px rgba(0,0,0,0.25);
    color: var(--slate); font-size: 15px; font-weight: 600;
    text-decoration: none; overflow: hidden; margin-top: -2px;
  }
  .btn-icon {
    width: 28px; height: 28px; border-radius: 14px 4px 4px 14px;
    background: linear-gradient(to bottom, var(--green-light), var(--green-dark));
    display: flex; align-items: center; justify-content: center;
    margin-right: 7px; flex: none;
  }
  .btn--active {
    background: linear-gradient(to bottom, var(--green-light), var(--green));
    color: #fff;
  }
  .btn--active .btn-icon { background: linear-gradient(to bottom, #777, #333); }

  .disclaimer {
    position: absolute; left: 428px; top: 587px; width: 382px; height: 109px;
    background: var(--note-bg); color: #fff;
    font-size: 11px; line-height: 11px; padding: 9px 12px 0 11px;
  }
  .disclaimer p { margin-bottom: 9px; }
  .disclaimer .indent { padding-left: 9px; text-indent: -9px; }
</style>
</head>
<body>
  <main class="email">
    <header class="brand">
      <span class="brand-name">CampusLedger.org</span>
    </header>

    <div class="title-band"><h1>Education &amp; Teaching Search</h1></div>
    <p class="aid-note">Financial Aid programs available for those who qualify.*</p>

    <div class="photo" role="img" aria-label="Photo of two students lying on a sunny lawn, one reading a green book, the other relaxing with a backpack"></div>

    <div class="head-band"></div>
    <table class="jobs">
      <thead>
        <tr>
          <th class="col-type">OCCUPANTION TYPE</th>
          <th class="col-salary">MEDIAN SALARY**</th>
          <th class="col-next">NEXT STEPS</th>
        </tr>
      </thead>
      <tbody>
        <tr>
          <td class="job">Elementary and Secondary<br>School Teachers</td>
          <td class="salary">$90,200 per year</td>
          <td class="next"><a class="btn btn--active" href="#"><span class="btn-icon"><svg width="12" height="10" viewBox="0 0 12 10"><path d="M1 1l4 4-4 4M6 1l4 4-4 4" fill="none" stroke="#fff" stroke-width="2"/></svg></span>See Programs</a></td>
        </tr>
        <tr>
          <td class="job">Educational, Guidance, School,<br>and Vocational Counselors</td>
          <td class="salary">$56,540 per year</td>
          <td class="next"><a class="btn" href="#"><span class="btn-icon"><svg width="12" height="10" viewBox="0 0 12 10"><path d="M1 1l4 4-4 4M6 1l4 4-4 4" fill="none" stroke="#2d4a05" stroke-width="2"/></svg></span>See Programs</a></td>
        </tr>
        <tr>
          <td class="job">Elementary School Teachers,<br>Except Special Education</td>
          <td class="salary">$55,270 per year</td>
          <td class="next"><a class="btn" href="#"><span class="btn-icon"><svg width="12" height="10" viewBox="0 0 12 10"><path d="M1 1l4 4-4 4M6 1l4 4-4 4" fill="none" stroke="#2d4a05" stroke-width="2"/></svg></span>See Programs</a></td>
        </tr>
        <tr>
          <td class="job">Preschool and Childcare<br>Centers</td>
          <td class="salary">$51,290 per year</td>
          <td class="next"><a class="btn" href="#"><span class="btn-icon"><svg width="12" height="10" viewBox="0 0 12 10"><path d="M1 1l4 4-4 4M6 1l4 4-4 4" fill="none" stroke="#2d4a05" stroke-width="2"/></svg></span>See Programs</a></td>
        </tr>
        <tr>
          <td class="job">Education Administrators</td>
          <td class="salary">$51,290 per year</td>
          <td class="next"><a class="btn" href="#"><span class="btn-icon"><svg width="12" height="10" viewBox="0 0 12 10"><path d="M1 1l4 4-4 4M6 1l4 4-4 4" fill="none" stroke="#2d4a05" stroke-width="2"/></svg></span>See Programs</a></td>
        </tr>
        <tr>
          <td class="job">Preschool Teachers (Except<br>Special Education)</td>
          <td class="salary">$30,150 per year</td>
          <td class="next"><a class="btn" href="#"><span class="btn-icon"><svg width="12" height="10" viewBox="0 0 12 10"><path d="M1 1l4 4-4 4M6 1l4 4-4 4" fill="none" stroke="#2d4a05" stroke-width="2"/></svg></span>See Programs</a></td>
        </tr>
      </tbody>
    </table>

    <aside class="disclaimer">
      <p class="indent">* &nbsp;Disclaimer: &nbsp;Financial Aid is available for those who qualify. To see if you qualify for financial aid of any kind you must speak with a representative of one of our partnering schools.</p>
      <p>** Median salaries according to the National Career Wage Survey</p>
      <p>Program outcomes vary according to each institution’s specific curriculum, and employment opportunities are not guaranteed.</p>
    </aside>
  </main>
</body>
</html>
```